OpenLeaf app needs an improved design

OpenLeaf makes available books that have been banned in certain countries. The current version of the app is available for download here: https://apps.vendrix-market.example/details?id=org.brightmoss.openleaf

At the moment, the app is available only in Chinese. Books are made available within the app, in text or audio format. Books can be downloaded for offline use. We created the app as a way to circumvent the intense censorship that is placed on book distribution inside China. The app is designed in such a way that the authorities are not able to censor the app, thus users in China are able to download the app, read content and receive updates to the app. So far over 100,000 people have used the app. Books are made available to the users for free and the app is also free to download.

We have used a similar anti-censorship strategy in a number of other apps, all with equally successful outcomes.

The app is only available on Android. While many Chinese purchase high end Android devices, Android is also the operating system of choice for new internet users in China. Oftentimes, the first time a user accesses the internet will be through an inexpensive Android smartphone.

This is very much a content driven app, with limited functionality but very visual. We need to optimize the app so that it is suitable for reading long texts. While we make available banned books through the app itself, our users are primarily avid readers - they are not likely to be netizens who wanted to download a book app just because it contains banned books. They will be readers who are interested in reading and exploring new books that are not normally available to them.

The app should have similar functionality to an e-reader, like a Pagette, however it needs to be optimized for smaller screens. Apps like Scrollnest present content in an easy to read format.

Target Market(s)

Our current end users are Chinese who are professionals and have an interest in reading. They are likely between the ages of 18-50. We try to make the app as easy and intuitive as possible. Even though there are over 700 million people online in China, another 600 million of them will come online soon. We want experienced internet and technology users to easily find the content they are looking for and we want new internet and technology users to be able to easily use the app. Our users mainly use the app in the comfort of their own home - as they would read an e-book (Pagette) or in a quiet cafe.

Industry/Entity Type

Book Publisher

Font styles to use
Serif

Colors

Designer to choose colors to be used in the design.

Requirements
Must have
• Our current challenges include:
• - We want to promote new books as well as popular books (and potentially other categories) and allow users to browse more books in that category.
• - Allow users to search.
• - For each book, we need an indication whether it is an audio book or a text book.
• - For each book, we need an indication whether the book has already been downloaded.
• Our current audio book challenges include:
• - Show book cover.
• - Include all standard audio playback functions (pause, play, next chapter etc).
• - Audio books can play in the background. When the user leaves this view, the app needs to indicate that an audio book is playing in the background, and show the user how to return to this interface (to pause playback, etc).
• Our current text book challenges include:
• - Show name of book.
• - Maximize use of screen (since it may be hard to read on a small device).
• - Allow user to easily navigate (next page, any page number etc).

```html
<!DOCTYPE html>
<html lang="zh-Hant">
<head>
<meta charset="utf-8">
<title>OpenLeaf — Reading Page</title>
<link rel="stylesheet" href="https://fonts.googleapis.com/css2?family=Noto+Sans+TC:wght@400;500&family=Roboto:wght@400;500&display=swap">
<style>
:root{
  --board:#b4dcf3;
  --ink:#111;
  --brand:#1a9be6;
  --status:#1496e2;
  --paper:#ffffff;
  --body-grey:#9a9a9a;
  --meta-grey:#8a8a8a;
  --night:#243044;
  --night-text:#dde3ea;
  --icon-grey:#8a97a6;
}
*{box-sizing:border-box;margin:0;padding:0}
html,body{width:1200px;height:806px;overflow:hidden}
body{background:var(--board);font-family:"Noto Sans TC","Roboto",sans-serif;color:var(--ink);position:relative}
.board-title{position:absolute;left:26px;top:22px;font:400 21px "Roboto",sans-serif}
.screen-label{position:absolute;top:749px;font:400 21px "Roboto",sans-serif}
.screen{position:absolute;top:80px;width:364px;height:646px;background:var(--paper);overflow:hidden}
.screen.night{background:var(--night);top:78px;height:648px;width:366px}
.status-bar{height:22px;background:var(--status);display:flex;justify-content:flex-end;align-items:center;gap:5px;padding-right:15px;color:#fff;font:500 13px "Roboto",sans-serif}
.app-bar{position:relative;height:46px}
.app-bar .back{position:absolute;left:18px;top:15px}
.app-bar .more{position:absolute;right:18px;top:14px}
.page-count{position:absolute;right:42px;top:18px;color:var(--brand);font:500 13px "Roboto",sans-serif;letter-spacing:.5px}
.book-title{position:absolute;left:18px;top:88px;font-size:20px;font-weight:400;letter-spacing:1.5px}
.read-all{position:absolute;left:274px;top:91px;width:72px;height:20px;border-radius:10px;background:var(--brand);color:#fff;font-size:10px;font-weight:500;display:flex;align-items:center;justify-content:center}
.book-meta{position:absolute;left:18px;top:117px;color:var(--meta-grey);font-size:13px}
.book-meta .sep{margin:0 6px;color:#bbb}
.cover{position:absolute;left:17px;top:151px;width:329px;height:145px;background:linear-gradient(90deg,#9a9ea3 0%,#d6d8da 35%,#3d3f42 55%,#6a6d71 75%,#c9cbcd 100%)}
.chapters{position:absolute;left:17px;top:322px;width:329px;list-style:none}
.chapter{position:relative;height:58.5px;font-size:12.5px;line-height:17px;padding-left:20px;color:#222}
.chapter .num{position:absolute;left:0;top:0;color:var(--meta-grey)}
.chapter .pages{position:absolute;right:0;top:0;font-family:"Roboto",sans-serif;font-size:13px}
.bottom-nav{position:absolute;left:0;right:0;bottom:0;height:56px;background:inherit}
.bottom-nav svg{position:absolute;top:16px}
.reader{position:absolute;left:17px;top:86px;width:330px;height:505px;overflow:hidden;font-size:13px;line-height:16.4px;text-align:justify;color:var(--body-grey);-webkit-mask-image:linear-gradient(#000 88%,transparent);mask-image:linear-gradient(#000 88%,transparent)}
.night .reader{color:var(--night-text)}
.reader p{margin-bottom:16.4px}
</style>
</head>
<body>

<h1 class="board-title">Reading Page</h1>

<section class="screen" style="left:24px">
  <div class="status-bar">
    <svg width="14" height="12" viewBox="0 0 14 12"><path d="M14 0V12H0Z" fill="#fff" opacity=".5"/><path d="M14 5V12H7Z" fill="#fff"/></svg>
    <svg width="14" height="11" viewBox="0 0 14 11"><path d="M0 2a10 10 0 0 1 14 0L7 11Z" fill="#fff"/></svg>
    <svg width="6" height="12" viewBox="0 0 6 12"><rect x="0" y="1" width="6" height="11" rx="1" fill="#fff"/><rect x="2" y="0" width="2" height="2" fill="#fff"/></svg>
    <span>09:00</span>
  </div>
  <div class="app-bar">
    <svg class="back" width="22" height="18" viewBox="0 0 22 18"><path d="M21 9H3M10 1 2 9l8 8" fill="none" stroke="var(--brand)" stroke-width="2.4"/></svg>
    <svg class="more" width="6" height="22" viewBox="0 0 6 22"><circle cx="3" cy="3" r="2.6" fill="var(--brand)"/><circle cx="3" cy="11" r="2.6" fill="var(--brand)"/><circle cx="3" cy="19" r="2.6" fill="var(--brand)"/></svg>
  </div>
  <h2 class="book-title">林遠山說出的秘密</h2>
  <div class="read-all">全部阅读</div>
  <p class="book-meta">周文瀾<span class="sep">|</span>100 pages</p>
  <div class="cover" role="img" aria-label="Book cover artwork in grey tones"></div>
  <ol class="chapters">
    <li class="chapter"><span class="num">1.</span>《林遠山說出的秘密：鮮為人知的故事》，<br>选读（一）<span class="pages">1 - 3</span></li>
    <li class="chapter"><span class="num">2.</span>《林遠山說出的秘密：鮮為人知的故事》，<br>选读（二）<span class="pages">4 - 5</span></li>
    <li class="chapter"><span class="num">3.</span>《林遠山說出的秘密：鮮為人知的故事》，<br>选读（三）<span class="pages">6 - 10</span></li>
    <li class="chapter"><span class="num">4.</span>《林遠山說出的秘密：鮮為人知的故事》，<br>选读（四）<span class="pages">11 - 20</span></li>
    <li class="chapter"><span class="num">5.</span>《林遠山說出的秘密：鮮為人知的故事》，<br><span style="opacity:.45">选读（五）</span><span class="pages">21 - 30</span></li>
  </ol>
  <nav class="bottom-nav">
    <svg style="left:55px" width="22" height="20" viewBox="0 0 22 20"><path d="M11 1 1 10h3v9h5v-6h4v6h5v-9h3Z" fill="var(--icon-grey)"/></svg>
    <svg style="left:140px" width="20" height="22" viewBox="0 0 20 22"><path d="M7 1h6v7h5l-8 8-8-8h5Z" fill="var(--brand)"/><rect x="1" y="18" width="18" height="3" fill="var(--brand)"/></svg>
    <svg style="left:225px" width="22" height="22" viewBox="0 0 22 22"><circle cx="9" cy="9" r="6.5" fill="none" stroke="var(--icon-grey)" stroke-width="2.4"/><path d="M14 14l6 6" stroke="var(--icon-grey)" stroke-width="2.8"/></svg>
    <svg style="left:312px" width="6" height="22" viewBox="0 0 6 22"><circle cx="3" cy="3" r="2.5" fill="var(--icon-grey)"/><circle cx="3" cy="11" r="2.5" fill="var(--icon-grey)"/><circle cx="3" cy="19" r="2.5" fill="var(--icon-grey)"/></svg>
  </nav>
</section>

<section class="screen" style="left:418px">
  <div class="status-bar">
    <svg width="14" height="12" viewBox="0 0 14 12"><path d="M14 0V12H0Z" fill="#fff" opacity=".5"/><path d="M14 5V12H7Z" fill="#fff"/></svg>
    <svg width="14" height="11" viewBox="0 0 14 11"><path d="M0 2a10 10 0 0 1 14 0L7 11Z" fill="#fff"/></svg>
    <svg width="6" height="12" viewBox="0 0 6 12"><rect x="0" y="1" width="6" height="11" rx="1" fill="#fff"/><rect x="2" y="0" width="2" height="2" fill="#fff"/></svg>
    <span>09:00</span>
  </div>
  <div class="app-bar">
    <svg class="back" width="22" height="18" viewBox="0 0 22 18"><path d="M21 9H3M10 1 2 9l8 8" fill="none" stroke="var(--brand)" stroke-width="2.4"/></svg>
    <span class="page-count">5 - 100</span>
    <svg class="more" width="6" height="22" viewBox="0 0 6 22"><circle cx="3" cy="3" r="2.6" fill="var(--brand)"/><circle cx="3" cy="11" r="2.6" fill="var(--brand)"/><circle cx="3" cy="19" r="2.6" fill="var(--brand)"/></svg>
  </div>
  <article class="reader">
    <p>的電影和一部電視連續劇 。</p>
    <p>一切都是爲了宣傳<br>塑慶“打黑”的光榮偉大和正確性。 重慶的普通幹警們也翹首以待，或許想從作品中感受到現實中很難獲得的成功感和英雄感在林遠山的治下，基層幹警不僅工作壓力繁重，而且時有“膽戰心驚”，唯恐丟了飯碗的緊迫感。重慶警察沈舒（音）就對計畫中的這部電影抱以很高的期待他口：“我們都知道，它會很棒，”“我們媒口，他們想讓梁家鳴（香港知名導演）來當導演。</p>
    <p>”沈舒說。 女導演何小虹也一度是熱門人選陳啟人口，書才是關鍵。</p>
    <p>他表示，這部書將是打黑運動的官方記載，因而極其重要，就像中國歷代皇帝下令編纂關於自己統治的官方歷史。</p>
    <p>“程西嶽想記錄下來，是誰在為這些黑社會性質的組織提供保護傘，”陳啟人在重慶接受採訪時口：“（其實就）是官員，”陳啟人負責撰寫的部分正是對此的回顧，被命名為《逆風之章》。</p>
    <p>林遠山還告訴他， 市領導知道腐敗的範圍 “他口，” 這場打黑運動僅僅只是第一步 。 我們還沒有進入深水區，” 陳啟人說 。</p>
    <p>但至於所謂的 “ 深水區究竟指什麼陳啟人也表示 “ 不知道 ” 但他隱晦地指出 ， 中國有些肥缺行業的掌門人往往是中共高層領導的子女 。2 陳啟人判斷 ， 這一系列出版計畫是林遠山的上司時任政治局委員的意思。</p>
  </article>
  <nav class="bottom-nav">
    <svg style="left:62px" width="20" height="22" viewBox="0 0 20 22"><path d="M10 1v19M2 12l8 8 8-8" fill="none" stroke="var(--icon-grey)" stroke-width="2.4"/></svg>
    <svg style="left:150px" width="20" height="22" viewBox="0 0 20 22"><path d="M10 21V2M2 10l8-8 8 8" fill="none" stroke="var(--icon-grey)" stroke-width="2.4"/></svg>
    <svg style="left:238px" width="22" height="22" viewBox="0 0 22 22"><circle cx="9" cy="9" r="6.5" fill="none" stroke="var(--icon-grey)" stroke-width="2.4"/><path d="M14 14l6 6" stroke="var(--icon-grey)" stroke-width="2.8"/></svg>
    <svg style="left:304px" width="24" height="24" viewBox="0 0 24 24"><path d="M12 1.5l2 3 3.5-1 .5 3.5 3.5.5-1 3.5 3 2-3 2 1 3.5-3.5.5-.5 3.5-3.5-1-2 3-2-3-3.5 1-.5-3.5-3.5-.5 1-3.5-3-2 3-2-1-3.5 3.5-.5.5-3.5 3.5 1Z" fill="var(--brand)"/><circle cx="12" cy="12" r="4" fill="#fff"/></svg>
  </nav>
</section>

<section class="screen night" style="left:810px">
  <div class="status-bar">
    <svg width="14" height="12" viewBox="0 0 14 12"><path d="M14 0V12H0Z" fill="#fff" opacity=".5"/><path d="M14 5V12H7Z" fill="#fff"/></svg>
    <svg width="14" height="11" viewBox="0 0 14 11"><path d="M0 2a10 10 0 0 1 14 0L7 11Z" fill="#fff"/></svg>
    <svg width="6" height="12" viewBox="0 0 6 12"><rect x="0" y="1" width="6" height="11" rx="1" fill="#fff"/><rect x="2" y="0" width="2" height="2" fill="#fff"/></svg>
    <span>09:00</span>
  </div>
  <div class="app-bar">
    <svg class="back" width="22" height="18" viewBox="0 0 22 18"><path d="M21 9H3M10 1 2 9l8 8" fill="none" stroke="var(--brand)" stroke-width="2.4"/></svg>
    <span class="page-count">5 - 100</span>
    <svg class="more" width="6" height="22" viewBox="0 0 6 22"><circle cx="3" cy="3" r="2.6" fill="var(--brand)"/><circle cx="3" cy="11" r="2.6" fill="var(--brand)"/><circle cx="3" cy="19" r="2.6" fill="var(--brand)"/></svg>
  </div>
  <article class="reader">
    <p>的電影和一部電視連續劇 。</p>
    <p>一切都是爲了宣傳<br>塑慶“打黑”的光榮偉大和正確性。 重慶的普通幹警們也翹首以待，或許想從作品中感受到現實中很難獲得的成功感和英雄感在林遠山的治下，基層幹警不僅工作壓力繁重，而且時有“膽戰心驚”，唯恐丟了飯碗的緊迫感。重慶警察沈舒（音）就對計畫中的這部電影抱以很高的期待他口：“我們都知道，它會很棒，”“我們媒口，他們想讓梁家鳴（香港知名導演）來當導演。</p>
    <p>”沈舒說。 女導演何小虹也一度是熱門人選陳啟人口，書才是關鍵。</p>
    <p>他表示，這部書將是打黑運動的官方記載，因而極其重要，就像中國歷代皇帝下令編纂關於自己統治的官方歷史。</p>
    <p>“程西嶽想記錄下來，是誰在為這些黑社會性質的組織提供保護傘，”陳啟人在重慶接受採訪時口：“（其實就）是官員，”陳啟人負責撰寫的部分正是對此的回顧，被命名為《逆風之章》。</p>
    <p>林遠山還告訴他， 市領導知道腐敗的範圍 “他口，” 這場打黑運動僅僅只是第一步 。 我們還沒有進入深水區，” 陳啟人說 。 但至於所謂的 “ 深水區究竟指什麼陳啟人也表示 “ 不知道 ” 但他隱晦地指出 ， 中國有些肥缺行業的掌門人往往是中共高層領導的子女 。2 陳啟人判斷 ， 這一系列出版計畫是林遠山的上司時任政治局委員兼市委書記程西嶽的意思 。 林遠山為 《 山城風雲紀實叢書 》 的作者們制定了</p>
  </article>
  <nav class="bottom-nav">
    <svg style="left:62px" width="20" height="22" viewBox="0 0 20 22"><path d="M10 1v19M2 12l8 8 8-8" fill="none" stroke="var(--icon-grey)" stroke-width="2.4"/></svg>
    <svg style="left:150px" width="20" height="22" viewBox="0 0 20 22"><path d="M10 21V2M2 10l8-8 8 8" fill="none" stroke="var(--icon-grey)" stroke-width="2.4"/></svg>
    <svg style="left:238px" width="22" height="22" viewBox="0 0 22 22"><circle cx="9" cy="9" r="6.5" fill="none" stroke="var(--icon-grey)" stroke-width="2.4"/><path d="M14 14l6 6" stroke="var(--icon-grey)" stroke-width="2.8"/></svg>
    <svg style="left:306px" width="20" height="26" viewBox="0 0 20 26"><path d="M3 1a12 12 0 0 1 0 24A9 12 0 0 0 3 1Z" fill="var(--brand)"/></svg>
  </nav>
</section>

<p class="screen-label" style="left:24px">5.0 Chapter List</p>
<p class="screen-label" style="left:412px">5.1 Reading Normal Mode</p>
<p class="screen-label" style="left:810px">5.2 Dark mode reading for night</p>

</body>
</html>
```